Fast growing Tech company needs redesign of Varnith's end user website!

We need to have our login screen, the dashboard, and the one page of the Varnith site to be redesigned for the end-users. Varnith is a document hosting service for title companies and real estate law firms. This allows the buyers and sellers to view their closing documents after closing along with many other features that help them out during the closing of their property. More information about what we do can be found on our test site https://qpx.482.sampledrafthost.example/. PLEASE NOTE: THE ABOVE SITE IS NOT THE ONE WE NEED REDONE. The above site is our corporate site that explains our service offering and we thought it would be helpful in providing you a better understanding of our service.
The site that we want to have redesigned is for the end user. THE SITE THAT NEEDS TO BE REDONE ARE THE SCREENSHOTS ATTACHED. We will need the login screen, dashboard, and the one page redesigned.
.
We will just need this in HTML and we will then do the rest for the placeholders for logos, data, mapping etc.
Overall, we want a new, fresh, and modern look for the website and we want the login screen, dashboard and one page website to be consistent in design. Again, these are the three screenshots that are attached.
For the winner, we will most likely need to hire you again for more sites because we have other versions.
Thank you and if any questions, please let us know.
Target Market(s)
This site is for buyer and sellers during the closing process of real estate transaction.

```html
<!DOCTYPE html>
<html lang="en">
<head>
<meta charset="utf-8">
<title>Varnith – Client Closing Portal</title>
<link href="https://fonts.googleapis.com/css2?family=Rubik:wght@300;400;500;700&display=swap" rel="stylesheet">
<style>
:root{
  --blue:#34a4d8;
  --blue-dark:#2b8fc0;
  --ink:#1f2a33;
  --muted:#6b7580;
  --line:#e3e7eb;
  --grey-bg:#f4f4f4;
  --navy:#0e1c27;
  --white:#fff;
}
*{box-sizing:border-box;margin:0;padding:0}
html,body{width:1200px;height:4444px;overflow:hidden;background:var(--white)}
body{font-family:'Rubik',sans-serif;color:var(--ink);position:relative}
.abs{position:absolute}

/* header / hero */
.brand{left:0;top:0;width:120px;height:74px;background:var(--blue);display:flex;align-items:center;justify-content:center;z-index:3}
.brand span{color:var(--white);font-size:22px;font-weight:400}
.hero-photo{left:0;top:0;width:1200px;height:600px;background:linear-gradient(160deg,#f3f4f5 0%,#d9dcdf 40%,#9ea4aa 75%,#6e757c 100%)}
.hero-card{left:720px;top:353px;width:480px;height:319px;background:var(--white);box-shadow:0 18px 40px rgba(0,0,0,.08)}
.hero-card .eyebrow{position:absolute;left:45px;top:44px;font-size:13px;font-weight:500;color:var(--blue)}
.hero-card h1{position:absolute;left:83px;top:80px;font-size:30px;font-weight:500;line-height:44px;color:var(--ink)}
.hero-card h1 u{text-decoration-color:var(--blue);text-decoration-thickness:3px;text-underline-offset:4px}
.client-mark{position:absolute;right:40px;top:248px;display:flex;align-items:center;gap:10px;font-size:16px;color:var(--ink)}
.client-mark i{width:18px;height:18px;background:#c0262d;display:block}

/* welcome */
.welcome{left:0;top:775px;width:1200px;text-align:center}
.welcome h2{font-size:24px;font-weight:500;color:var(--blue);margin-bottom:24px}
.welcome p{width:620px;margin:0 auto;font-size:12px;font-weight:300;line-height:22px;color:var(--muted)}

/* map + transaction */
.map-band{left:0;top:953px;width:1200px;height:478px;background:#f1f3f4}
.map{left:520px;top:953px;width:680px;height:478px;background:linear-gradient(90deg,#eef1f3 0%,#e5e9ec 55%,#cfe6f3 80%,#a8d6ef 100%)}
.txn-card{left:169px;top:1022px;width:319px;height:481px;background:var(--blue);border-radius:30px 0 40px 0;padding:42px 34px;color:var(--white)}
.txn-card h3{font-size:14px;font-weight:500;margin-bottom:14px}
.txn-card p{font-size:10.5px;font-weight:500;line-height:26px}
.txn-card hr{border:0;border-top:1px solid rgba(255,255,255,.35);margin:14px 0 22px}
.txn-card .gap{height:28px}

/* milestones */
.milestones{left:0;top:1607px;width:1200px;height:517px;background:var(--grey-bg);border-radius:60px 0 60px 0}
.section-title{font-size:24px;font-weight:500;color:var(--blue);text-align:center}
.milestones .section-title{position:absolute;top:46px;width:100%}
.node{width:16px;height:16px;border-radius:50%;border:1px solid #b9dcee;background:var(--white);display:flex;align-items:center;justify-content:center}
.node::after{content:"";width:6px;height:6px;border-radius:50%;background:var(--blue)}
.node.todo{border-color:#d5d9dc}
.node.todo::after{background:#bfc5ca}
.step{width:200px;text-align:center}
.step b{display:block;font-size:14px;font-weight:400;line-height:22px;color:var(--ink)}
.step em{display:block;font-style:normal;font-size:10px;font-weight:500;margin-top:8px;color:var(--blue)}
.step em.todo{color:#b5bcc2}

/* documents + wiring */
.docs{left:169px;top:2360px;width:386px}
.docs h3{font-size:19px;font-weight:500;text-align:center;margin-bottom:36px}
.doc-row{display:flex;align-items:center;gap:22px;height:97px;border-top:1px solid var(--line);padding-left:0}
.doc-row:last-child{border-bottom:1px solid var(--line)}
.doc-row span{font-size:19px;font-weight:500}
.wiring{left:600px;top:2240px;width:479px;height:522px;background:var(--blue);border-radius:40px 0 40px 0;color:var(--white);padding:46px 50px 0}
.wiring h3{font-size:18px;font-weight:500;text-align:center;margin-bottom:36px}
.wire-row{height:52px;border-top:1px solid rgba(255,255,255,.22);font-size:13px;font-weight:500;display:flex;align-items:center}
.wire-row.link{font-size:11px}

/* team */
.agent{top:2888px;width:260px;height:391px;overflow:hidden}
.agent .photo{position:absolute;inset:0;background:linear-gradient(180deg,#5d6a75 0%,#8f99a1 55%,#3d4a56 100%)}
.agent .info{position:absolute;left:0;bottom:0;width:260px;height:150px;background:rgba(52,164,216,.85);border-radius:40px 0 0 0;color:var(--white);text-align:center;padding-top:18px}
.agent .info strong{display:block;font-size:17px;font-weight:500}
.agent .info small{display:block;font-size:13px;font-weight:300;margin-top:6px}
.agent .info p{font-size:13px;font-weight:300;line-height:22px;margin-top:26px}

/* checklists */
.list{width:379px}
.list h3{font-size:19px;font-weight:500;text-align:center;margin-bottom:34px}
.item{position:relative;height:74px;border-bottom:1px solid var(--line);padding-top:2px}
.item:last-child{border-bottom:0}
.item .task{font-size:13px;font-weight:300;color:#4a545c;letter-spacing:.3px}
.item .state{font-size:10px;font-weight:500;color:var(--blue);margin-top:8px}
.item .state.todo{color:#b5bcc2}
.item .node{position:absolute;right:0;top:6px;width:22px;height:22px}
.add-note{font-size:11px;font-weight:300;color:var(--muted);margin-top:14px}
.divider-v{left:600px;top:3526px;width:1px;height:181px;background:#cfe4ef}

/* faq */
.faq{left:121px;top:3908px;width:958px;height:471px;background:var(--navy);border-radius:52px 0 52px 0;color:var(--white)}
.faq h3{position:absolute;top:56px;width:100%;text-align:center;font-size:24px;font-weight:500}
.faq-list{position:absolute;left:94px;top:138px;width:768px}
.qa{border-top:1px solid rgba(255,255,255,.14);padding:28px 0 30px;position:relative}
.qa:last-child{border-bottom:1px solid rgba(255,255,255,.14)}
.qa h4{font-size:16px;font-weight:500;color:var(--blue)}
.qa .toggle{position:absolute;right:0;top:28px;color:var(--blue);font-size:16px}
.qa p{font-size:12.5px;font-weight:300;line-height:24px;margin-top:14px;width:660px}
</style>
</head>
<body>

<div class="abs hero-photo" role="img" aria-label="Photograph of a modern glass office tower against a pale sky"></div>
<div class="abs brand"><span>Varnith</span></div>
<div class="abs hero-card">
  <div class="eyebrow">CLIENT PROJECT 1</div>
  <h1>Building a Brighter<br><u>Future Project &amp; Good</u><br>Support.</h1>
  <div class="client-mark"><i></i>Meridian Law Academy</div>
</div>

<section class="abs welcome">
  <h2>WELCOME CLARK BUYER</h2>
  <p>We have traded more than 850 properties around the UK at a value of more than £118 million. Our success rate on our trading portfolio has been more than 95% and our investments in land are executed with the same approach of smart investing.</p>
</section>

<div class="abs map-band"></div>
<div class="abs map" role="img" aria-label="Street map of the city showing the property locations with pins"></div>
<aside class="abs txn-card">
  <h3>YOUR TRANSACTION INFORMATION</h3>
  <p>File Number: 2018-015987</p>
  <p>Buyer: Clark Buyer</p>
  <p>Seller: Chloe Seller</p>
  <p>Agen: Bob buyer agen</p>
  <hr>
  <h3>PROPERTY ADDRESS</h3>
  <p>File Number: 2018-015987</p>
  <p>Buyer: Clark Buyer</p>
  <div class="gap"></div>
  <h3>PURCHASE DETAILS</h3>
  <p>File Number: 2018-015987</p>
  <p>Buyer: Clark Buyer</p>
</aside>

<section class="abs milestones">
  <h2 class="section-title">CLOSING MILESTONE</h2>
  <svg class="abs" style="left:0;top:0" width="1200" height="517" aria-hidden="true">
    <g fill="none" stroke="#c9ced2" stroke-width="1" stroke-dasharray="3 3">
      <line x1="268" y1="143" x2="938" y2="143"/>
      <path d="M946 143 H1016 Q1031 143 1031 158 V355 Q1031 370 1016 370 H720"/>
    </g>
  </svg>
  <div class="abs node" style="left:252px;top:135px"></div>
  <div class="abs node" style="left:478px;top:135px"></div>
  <div class="abs node todo" style="left:704px;top:135px"></div>
  <div class="abs node todo" style="left:930px;top:135px"></div>
  <div class="abs node todo" style="left:704px;top:362px"></div>
  <div class="abs node todo" style="left:930px;top:362px"></div>

  <div class="abs step" style="left:167px;top:176px"><b>Trancasction Started</b><em>COMPLETED</em></div>
  <div class="abs step" style="left:386px;top:176px"><b>Earnest Money<br>Received</b><em>COMPLETED</em></div>
  <div class="abs step" style="left:612px;top:176px"><b>Delivered Title<br>Report</b><em class="todo">NOT COMPLETED</em></div>
  <div class="abs step" style="left:838px;top:176px"><b>Title Cleared</b><em class="todo">NOT COMPLETED</em></div>
  <div class="abs step" style="left:612px;top:403px"><b>Transaction<br>Closed</b><em class="todo">NOT COMPLETED</em></div>
  <div class="abs step" style="left:838px;top:403px"><b>Signing Scedule</b><em class="todo">NOT COMPLETED</em></div>
</section>

<section class="abs docs">
  <h3>DOCUMENTS YOU NEED TO VIEW</h3>
  <div class="doc-row">
    <svg width="38" height="48" viewBox="0 0 38 48" aria-hidden="true"><path d="M2 2 H26 L36 12 V46 H2 Z M26 2 V12 H36" fill="none" stroke="var(--blue)" stroke-width="2" stroke-linejoin="round"/></svg>
    <span>Closing paper work</span>
  </div>
  <div class="doc-row">
    <svg width="38" height="48" viewBox="0 0 38 48" aria-hidden="true"><path d="M2 2 H26 L36 12 V46 H2 Z M26 2 V12 H36" fill="none" stroke="var(--blue)" stroke-width="2" stroke-linejoin="round"/></svg>
    <span>Purchase Agreement</span>
  </div>
</section>

<section class="abs wiring">
  <h3>WIRING INSTRUCTIONS</h3>
  <div class="wire-row">Bank Name:</div>
  <div class="wire-row">Bank Address:</div>
  <div class="wire-row">Bank Phone:</div>
  <div class="wire-row">Bank Aba Number:</div>
  <div class="wire-row">Account Number:</div>
  <div class="wire-row">Any Additional Information:</div>
  <div class="wire-row link">Download Wire Intructions Document</div>
</section>

<article class="abs agent" style="left:121px">
  <div class="photo" role="img" aria-label="Portrait photo of a smiling team member in a light shirt"></div>
  <div class="info"><strong>Hannah Pryce</strong><small>The Real Estate Law Firm</small><p>hannah.pryce@example.com<br>555-010-2040</p></div>
</article>
<article class="abs agent" style="left:470px">
  <div class="photo" role="img" aria-label="Portrait photo of a smiling team member in a red top"></div>
  <div class="info"><strong>Hannah Pryce</strong><small>The Real Estate Law Firm</small><p>hannah.pryce@example.com<br>555-010-2040</p></div>
</article>
<article class="abs agent" style="left:819px">
  <div class="photo" role="img" aria-label="Portrait photo of a team member on a dark background"></div>
  <div class="info"><strong>Hannah Pryce</strong><small>The Real Estate Law Firm</small><p>hannah.pryce@example.com<br>555-010-2040</p></div>
</article>

<section class="abs list" style="left:171px;top:3386px">
  <h3>MOVING CHECKLIST</h3>
  <div class="item"><div class="task">ADDRESS CHANGE - POST OFFICE</div><div class="state">COMPLETED</div><span class="node"></span></div>
  <div class="item"><div class="task">ADDRESS CHANGE - BANK</div><div class="state">COMPLETED</div><span class="node"></span></div>
  <div class="item"><div class="task">ADDRESS CHANGE - CREDIT CARD COMPANIES</div><div class="state">COMPLETED</div><span class="node"></span></div>
  <div class="item"><div class="task">ADDRESS CHANGE - FRIENDS / RELATIVE</div><div class="state">COMPLETED</div><span class="node"></span></div>
  <div class="item"><div class="task">ADDRESS CHANGE - LIFE INSURANCE</div><div class="state">COMPLETED</div><span class="node"></span></div>
</section>
<div class="abs divider-v"></div>
<section class="abs list" style="left:652px;top:3386px">
  <h3>MOVING WISHLIST</h3>
  <div class="item"><div class="task">NEED TO CALL ROOFING COMPANY</div><div class="state todo">NOT COMPLETED</div><span class="node todo"></span></div>
  <div class="item"><div class="task">CALL FLORING COMPANY</div><div class="state todo">NOT COMPLETED</div><span class="node todo"></span></div>
  <div class="add-note">Add items to wishlist</div>
</section>

<section class="abs faq">
  <h3>FREQUENTLY ASKED QUESTION</h3>
  <div class="faq-list">
    <div class="qa">
      <h4>WHAT SHOULD I EXPECT AT CLOSING?</h4><span class="toggle">–</span>
      <p>Lorem ipsum dolor sit amet, consectetur adipiscing elit, sed do eiusmod tempor incididunt ut labore et dolore magna aliqua. Ut enim ad minim veniam, quis nostrud exercitation ullamco laboris nisi ut aliquip ex ea commodo consequat.</p>
    </div>
    <div class="qa">
      <h4>WHAT TITLE INSURANCE</h4><span class="toggle">+</span>
    </div>
  </div>
</section>

</body>
</html>
```